Digital Asset Exchange (Trading Platform)

We need a design of Digital Asset Exchange Trading Platform.

Please find attached a mock up of LumaVoltix design this has to be redesigned based on fenrow.example style.

Industry/Entity Type

Digital

```html
<!DOCTYPE html>
<html lang="en">
<head>
<meta charset="utf-8">
<title>LumaVoltix – Digital Asset Exchange</title>
<link href="https://fonts.googleapis.com/css2?family=Open+Sans:wght@400;600;700&display=swap" rel="stylesheet">
<style>
:root{
  --brand:#1d9fd8;
  --bg:#333333;
  --black:#050505;
  --panel:#4d4d4d;
  --row-a:#5a5a5a;
  --row-b:#4e4e4e;
  --head:#2a6580;
  --orange:#f39a1e;
  --green:#2f7d0b;
  --red:#8e0b0b;
  --up:#38d12a;
  --down:#e02020;
  --text:#ffffff;
  --muted:#cfcfcf;
  --amber:#f0a020;
}
*{margin:0;padding:0;box-sizing:border-box}
html,body{width:1200px;height:639px;overflow:hidden;background:var(--bg);font-family:"Open Sans",Arial,sans-serif;color:var(--text)}
.abs{position:absolute}
.site-header{position:absolute;left:0;top:0;width:1200px;height:46px;background:var(--brand)}
.brand{position:absolute;left:160px;top:5px;display:flex;align-items:center;gap:8px}
.brand-dot{width:36px;height:36px;border-radius:50%;background:#fff}
.brand-name{font-size:24px;font-weight:400;color:#fff}
.main-nav{position:absolute;top:16px;font-size:11.5px;letter-spacing:.3px}
.user-box{position:absolute;left:975px;top:0;width:54px;height:46px;border-left:1px solid #fff;border-right:1px solid #fff}
.balance-bar{position:absolute;left:0;top:46px;width:1200px;height:48px;background:var(--black)}
.balance-title{position:absolute;left:163px;top:14px;font-size:17px;color:var(--brand)}
.wallet{position:absolute;top:2px;height:44px;background:#1a1a1a;font-size:11px;display:flex;align-items:center;justify-content:space-between;padding:0 8px}
.limit-box{position:absolute;top:4px;width:93px;height:42px;background:#1a1a1a;text-align:center}
.limit-box small{display:block;font-size:9px;color:var(--amber);margin-top:2px}
.limit-box b{font-size:18px;font-weight:400}
.field{position:absolute;left:860px;width:169px;height:15px;border:1px solid #666;background:#222;font-size:9px;color:var(--amber);padding-left:5px;line-height:13px}
.tabs{position:absolute;top:100px;height:28px;font-size:14px;line-height:28px;text-align:center}
.tab-active{background:var(--brand)}
.orders{position:absolute;left:159px;top:128px;width:402px;font-size:11px}
.orders .row{display:flex;height:26px;line-height:26px;padding-left:13px;border-bottom:1px solid #3a3a3a}
.orders .th{background:var(--head);font-size:12px;height:27px;line-height:27px}
.orders .row:nth-child(even){background:var(--row-a)}
.orders .row:nth-child(odd):not(.th){background:var(--row-b)}
.c1{width:87px}.c2{width:126px}.c3{width:118px}
.pairs{position:absolute;left:159px;top:256px;width:402px;height:50px;background:var(--panel);font-size:11px}
.pair-label{position:absolute;left:0;width:62px;height:25px;line-height:25px;padding-left:10px;font-size:14px}
.pair-col{position:absolute;width:90px;text-align:center}
.social{position:absolute;left:159px;top:329px;width:402px;height:90px;background:var(--panel)}
.social-tab{position:absolute;top:0;height:25px;line-height:25px;font-size:14px;padding-left:36px}
.feed{position:absolute;left:0;top:26px;width:402px;height:64px;background:#555;font-size:12px;padding:17px 0 0 65px;line-height:13px}
.avatar{position:absolute;left:16px;top:14px;width:35px;height:35px;background:linear-gradient(#dcdcdc,#777)}
.chart{position:absolute;left:593px;top:100px;width:436px;height:319px;background:var(--black)}
.ctl{position:absolute;top:6px;height:18px;border:1px solid #777;background:#222;font-size:10px;line-height:16px;padding-left:4px}
.book{position:absolute;left:159px;top:449px;font-size:11px}
.book-row{display:flex;height:24px;line-height:24px;margin-bottom:1px}
.book-label{width:75px;background:var(--black);padding-left:12px;font-size:14px}
.cell{width:56.8px;text-align:center}
.g{background:var(--green)}.r{background:var(--red)}
.site-footer{position:absolute;left:159px;top:590px;width:870px;height:46px;background:var(--black);font-size:11.5px;line-height:46px}
</style>
</head>
<body>
<header class="site-header">
  <div class="brand"><span class="brand-dot"></span><span class="brand-name">LumaVoltix</span></div>
  <nav>
    <span class="main-nav" style="left:658px">HOME</span>
    <span class="main-nav" style="left:725px">FEATURES</span>
    <span class="main-nav" style="left:809px">SECURITY</span>
    <span class="main-nav" style="left:891px">SUPPORT</span>
  </nav>
  <div class="user-box">
    <svg width="54" height="46" viewBox="0 0 54 46"><circle cx="27" cy="17" r="6" fill="#fff"/><path d="M16 36c0-8 5-11 11-11s11 3 11 11z" fill="#fff"/><path d="M27 26l-2 8 2 2 2-2z" fill="var(--brand)"/></svg>
  </div>
</header>

<section class="balance-bar">
  <span class="balance-title">Your Balance</span>
  <div class="wallet" style="left:276px;width:92px;border-bottom:2px solid #2aa7e6"><span>BTC</span><span>0.92176</span></div>
  <div class="wallet" style="left:371px;width:93px;border-bottom:2px solid #2c3fd0"><span>LTC</span><span>0.92176</span></div>
  <div class="wallet" style="left:467px;width:92px;border-bottom:2px solid #a23bd0"><span>USD</span><span>1987.45</span></div>
  <span class="abs" style="left:572px;top:14px;font-size:17px;color:var(--brand)">&#9662; Market</span>
  <div class="limit-box" style="left:655px;border-bottom:3px solid var(--down)"><small>Limit Sell &nbsp;Qty: 20</small><b><span style="color:var(--down)">&#8595;</span> 1575.60</b></div>
  <div class="limit-box" style="left:753px;border-bottom:3px solid var(--up)"><small>Limit Sell &nbsp;Qty: 20</small><b><span style="color:var(--up)">&#8593;</span> 1575.60</b></div>
  <div class="field" style="top:8px">Qty: &nbsp;&nbsp;&nbsp;&nbsp;&nbsp;&nbsp;20</div>
  <div class="field" style="top:27px">Limit: &nbsp;&nbsp;1576.63</div>
</section>

<div class="tabs tab-active" style="left:159px;width:81px">Orders</div>
<div class="tabs" style="left:250px;width:86px">History</div>
<div class="tabs" style="left:345px;width:106px">Transactions</div>

<div class="orders">
  <div class="row th"><span class="c1">Ticker</span><span class="c2">Time</span><span class="c3">Price &#9652;</span><span>Volume &#9662;</span></div>
  <div class="row"><span class="c1">BTC / USD</span><span class="c2">12:23 12.10.2014</span><span class="c3">634.43</span><span>O.23</span></div>
  <div class="row"><span class="c1">BTC / USD</span><span class="c2">12:23 12.10.2014</span><span class="c3">634.43</span><span>O.23</span></div>
  <div class="row"><span class="c1">BTC / USD</span><span class="c2">12:23 12.10.2014</span><span class="c3">634.43</span><span>O.23</span></div>
</div>

<div class="pairs">
  <div class="pair-label" style="top:0;background:var(--brand)">Pair</div>
  <div class="pair-label" style="top:25px;background:var(--orange)">Price</div>
  <svg class="abs" style="left:67px;top:17px" width="16" height="16"><circle cx="8" cy="8" r="7.5" fill="#111"/><path d="M11 8H5M7.5 5L4.5 8l3 3" stroke="#fff" stroke-width="1.5" fill="none"/></svg>
  <svg class="abs" style="left:381px;top:17px" width="16" height="16"><circle cx="8" cy="8" r="7.5" fill="#111"/><path d="M5 8h6M8.5 5l3 3-3 3" stroke="#fff" stroke-width="1.5" fill="none"/></svg>
  <span class="pair-col" style="left:91px;top:7px">BTC / USD</span>
  <span class="pair-col" style="left:185px;top:7px">LTC / USD</span>
  <span class="pair-col" style="left:283px;top:7px">LTC / BTC</span>
  <span class="pair-col" style="left:91px;top:32px"><span style="color:var(--down)">&#8595;</span> 634.12</span>
  <span class="pair-col" style="left:185px;top:32px"><span style="color:var(--down)">&#8595;</span> 23.23</span>
  <span class="pair-col" style="left:283px;top:32px"><span style="color:var(--up)">&#8593;</span> 0.0123</span>
</div>

<div class="social">
  <div class="social-tab" style="left:0;width:93px;background:var(--brand)">Chirpline</div>
  <svg class="abs" style="left:10px;top:6px" width="16" height="14"><rect width="16" height="14" fill="#fff" rx="2"/></svg>
  <div class="social-tab" style="left:94px;width:92px;background:#777">News</div>
  <svg class="abs" style="left:104px;top:6px" width="20" height="14"><rect x="1" y="1" width="18" height="12" fill="none" stroke="#fff" stroke-width="1.5"/><path d="M4 5h5M4 8h5M11 5h5M11 8h5" stroke="#fff"/></svg>
  <div class="social-tab" style="left:188px;width:93px;background:#999">Chat</div>
  <svg class="abs" style="left:196px;top:5px" width="20" height="15"><ellipse cx="10" cy="7" rx="9" ry="6" fill="#fff"/><path d="M4 11l-2 4 5-3z" fill="#fff"/></svg>
  <div class="feed">
    <div class="avatar" role="img" aria-label="User profile photo"></div>
    If computers get too powerful, we can organize them into committees. That'll do them in.
    <span class="abs" style="left:394px;top:19px;width:3px;height:22px;background:#fff"></span>
  </div>
</div>

<div class="chart">
  <div class="ctl" style="left:6px;width:80px;background:#fff;border:0"></div>
  <div class="ctl" style="left:86px;width:40px;color:#fff">1D <span style="float:right;padding-right:3px">&#9662;</span></div>
  <div class="ctl" style="left:138px;width:80px">Chart <span style="float:right;padding-right:3px">&#9662;</span></div>
  <div class="ctl" style="left:229px;width:79px">Studies <span style="float:right;padding-right:3px">&#9662;</span></div>
  <div class="ctl" style="left:319px;width:54px">&#9881; <span style="float:right;padding-right:3px">&#9662;</span></div>
  <div class="ctl" style="left:384px;width:34px;text-align:center;padding:0">F</div>
  <div class="ctl" style="left:10px;top:38px;width:82px;height:22px;line-height:20px;font-size:9px;background:#333">Select Tool</div>
  <div class="abs" style="left:246px;top:38px;font-size:8.5px;line-height:12px;color:#ddd">O: &nbsp;141.93 &nbsp;&nbsp;&nbsp;&nbsp;&nbsp;H: &nbsp;142.10 &nbsp;&nbsp;&nbsp;&nbsp;V: &nbsp;119.9m<br>C: &nbsp;141.02 &nbsp;&nbsp;&nbsp;&nbsp;&nbsp;L: &nbsp;&nbsp;140.80</div>
  <svg class="abs" style="left:0;top:66px" width="436" height="253" viewBox="0 0 436 253">
    <g stroke="#2a2a2a">
      <path d="M0 20H400M0 37H400M0 54H400M0 71H400M0 88H400M0 105H400M0 122H400M0 139H400M0 156H400M0 173H400M0 190H400M0 208H400"/>
      <path d="M10 0V230M90 0V230M180 0V230M260 0V230M345 0V230"/>
    </g>
    <g font-size="8" fill="#ddd">
      <text x="404" y="6">148.00</text><text x="404" y="23">147.00</text><text x="404" y="40">146.00</text><text x="404" y="57">145.00</text><text x="404" y="74">144.00</text><text x="404" y="91">143.00</text><text x="404" y="125">141.00</text><text x="404" y="142">140.00</text><text x="404" y="159">139.00</text><text x="404" y="176">138.00</text><text x="404" y="193">137.00</text><text x="404" y="211">129.00</text>
      <text x="0" y="251">ul</text><text x="82" y="251">aug</text><text x="173" y="251">sep</text><text x="253" y="251">oct</text><text x="337" y="251">nov</text>
    </g>
    <rect x="401" y="97" width="30" height="12" fill="#5aa83a"/><text x="405" y="106" font-size="8" fill="#fff">142.14</text>
    <g stroke-width="1">
      <g fill="#9ed97a" stroke="#9ed97a">
        <rect x="12" y="180" width="3" height="12"/><rect x="50" y="172" width="3" height="16"/><rect x="80" y="165" width="3" height="18"/><rect x="96" y="160" width="3" height="14"/><rect x="108" y="130" width="3" height="14"/><rect x="116" y="125" width="3" height="12"/><rect x="126" y="110" width="3" height="18"/><rect x="140" y="100" width="3" height="14"/><rect x="150" y="95" width="3" height="18"/><rect x="168" y="110" width="3" height="14"/><rect x="190" y="70" width="3" height="20"/><rect x="200" y="62" width="3" height="14"/><rect x="210" y="20" width="3" height="40"/><rect x="228" y="36" width="3" height="14"/><rect x="248" y="65" width="3" height="16"/><rect x="262" y="52" width="3" height="20"/><rect x="300" y="55" width="3" height="14"/><rect x="310" y="32" width="3" height="20"/><rect x="332" y="100" width="3" height="16"/><rect x="352" y="86" width="3" height="20"/><rect x="396" y="150" width="3" height="30"/>
      </g>
      <g fill="#d4281c" stroke="#d4281c">
        <rect x="30" y="180" width="3" height="14"/><rect x="70" y="170" width="3" height="14"/><rect x="88" y="172" width="3" height="12"/><rect x="132" y="112" width="3" height="12"/><rect x="176" y="116" width="3" height="14"/><rect x="218" y="26" width="3" height="18"/><rect x="238" y="40" width="3" height="22"/><rect x="256" y="60" width="3" height="16"/><rect x="276" y="18" width="3" height="30"/><rect x="288" y="62" width="3" height="22"/><rect x="322" y="80" width="3" height="30"/><rect x="342" y="82" width="3" height="26"/><rect x="362" y="110" width="3" height="40"/><rect x="372" y="150" width="3" height="22"/><rect x="382" y="170" width="3" height="16"/>
      </g>
    </g>
    <circle cx="118" cy="219" r="7" fill="#ddd"/><path d="M114 219h8" stroke="#000" stroke-width="1.5"/>
    <path d="M131 221l38-3v3z" fill="#777"/>
    <circle cx="184" cy="219" r="7" fill="#ddd"/><path d="M180 219h8M184 215v8" stroke="#000" stroke-width="1.5"/>
    <rect x="402" y="228" width="30" height="19" rx="2" fill="#bbb"/><path d="M409 237h10M415 233l4 4-4 4M423 232v10" stroke="#fff" stroke-width="1.5" fill="none"/>
  </svg>
</div>

<div class="book">
  <div class="book-row"><span class="book-label">Price</span>
    <span class="cell g">634.12</span><span class="cell g">634.12</span><span class="cell g">634.12</span><span class="cell g">634.12</span><span class="cell g">634.12</span><span class="cell g">634.12</span><span class="cell g">634.12</span><span class="cell r">634.12</span><span class="cell r">634.12</span><span class="cell r">634.12</span><span class="cell r">634.12</span><span class="cell r">634.12</span><span class="cell r">634.12</span><span class="cell r">634.12</span>
  </div>
  <div class="book-row"><span class="book-label">Volume</span>
    <span class="cell g">0.223</span><span class="cell g">0.223</span><span class="cell g">0.223</span><span class="cell g">0.223</span><span class="cell g">0.223</span><span class="cell g">0.223</span><span class="cell g">0.223</span><span class="cell r">0.223</span><span class="cell r">0.223</span><span class="cell r">0.223</span><span class="cell r">0.223</span><span class="cell r">0.223</span><span class="cell r">0.223</span><span class="cell r">0.223</span>
  </div>
</div>

<footer class="site-footer">
  <span class="abs" style="left:20px">2014 &nbsp;LumaVoltix.</span>
  <span class="abs" style="left:651px">About</span>
  <span class="abs" style="left:707px">Terms &amp; Conditions</span>
  <span class="abs" style="left:827px">FAQ</span>
</footer>
</body>
</html>
```